Business Card Design

I need a business card for company that is a limited company that was originally an off-road vehicle company (atv's side by sides snowmobiles and motorcycles) and I have recently sold the assets of the company that was operating under a different name and have become semi retired. I continue to do maintenance on these types of vehicles and also sell and install parts and accessories. Recently I have also contracted to a snowmobile club to operate their groomer to groom the snowmobile trails. I would like bright and bold colors.
Industry/Entity Type
Club
Contact Information for Business Card
KTV Holdings Ltd.
Milo Fenwick
780-413-2769

```html
<!DOCTYPE html>
<html lang="en">
<head>
<meta charset="utf-8">
<title>KTV Holdings Ltd. – Business Card</title>
<link href="https://fonts.googleapis.com/css2?family=Michroma&display=swap" rel="stylesheet">
<style>
  :root {
    --page: #c9c9cd;
    --card-dark: #0b151b;
    --card-mid: #14313b;
    --brand-red: #e8203a;
    --text-light: #e6e6e6;
    --text-muted: #b9c0c4;
    --icon-orange: #ef4a1d;
    --icon-green: #2f8d3a;
    --photo-snow: #d9434a;
    --photo-moto: #e0812e;
  }
  * { box-sizing: border-box; margin: 0; padding: 0; }
  html, body { width: 1200px; height: 800px; overflow: hidden; }
  body {
    background: var(--page);
    font-family: "Michroma", sans-serif;
    position: relative;
  }
  .card {
    position: absolute;
    left: 290px;
    width: 620px;
    height: 354px;
    border-radius: 3px;
    background:
      radial-gradient(circle at 45% 35%, rgba(40,90,105,.35), transparent 55%),
      radial-gradient(circle at 62% 78%, rgba(40,90,105,.3), transparent 45%),
      linear-gradient(135deg, var(--card-mid), var(--card-dark) 80%);
    box-shadow: 0 6px 18px rgba(0,0,0,.25);
    overflow: hidden;
    color: var(--text-light);
  }
  .card--back { top: 36px; }
  .card--front { top: 410px; }

  .brand-name {
    color: var(--brand-red);
    font-size: 38px;
    letter-spacing: 2px;
    white-space: nowrap;
  }
  .card--back .brand-name {
    position: absolute;
    left: 0; right: 0; top: 145px;
    text-align: center;
  }
  .back-dots {
    position: absolute; right: 40px; top: 44px;
    display: flex; gap: 6px;
  }
  .back-dots span {
    width: 32px; height: 32px; border-radius: 50%;
    background: #2b3338;
  }
  .back-dots span:last-child { margin-top: 22px; }

  .services {
    position: absolute; left: 34px; top: 30px; width: 262px;
  }
  .service-photos { display: flex; gap: 20px; margin-bottom: 18px; }
  .service-photo {
    width: 76px; height: 76px; border-radius: 50%;
    border: 3px solid #fff;
  }
  .service-photo--snow { background: radial-gradient(circle, var(--photo-snow) 20%, #f3f3f3 65%); }
  .service-photo--moto { background: radial-gradient(circle, var(--photo-moto) 20%, #f3f3f3 65%); }
  .service-types { font-size: 12px; letter-spacing: .5px; margin-bottom: 22px; white-space: nowrap; }
  .service-list { list-style: none; }
  .service-list li {
    display: flex; gap: 14px; align-items: flex-start;
    font-size: 11px; color: var(--text-muted); letter-spacing: 1px;
    margin-bottom: 12px; line-height: 1.6;
  }
  .service-list svg { flex: none; }

  .identity {
    position: absolute; left: 312px; right: 18px; top: 86px;
  }
  .identity .brand-name { font-size: 19px; letter-spacing: 1px; margin-bottom: 26px; }
  .person-name { font-size: 17px; letter-spacing: 2px; color: var(--text-light); margin-bottom: 10px; white-space: nowrap; }
  .person-bio { font-size: 8px; line-height: 1.7; color: var(--text-light); letter-spacing: .5px; margin-bottom: 22px; }
  .contact-row {
    display: flex; align-items: center; gap: 12px;
    font-size: 14px; color: var(--brand-red); margin-bottom: 10px; white-space: nowrap;
  }
  .contact-row--email { font-size: 11px; }
  .contact-icon {
    width: 20px; height: 20px; flex: none;
    clip-path: polygon(25% 0,75% 0,100% 50%,75% 100%,25% 100%,0 50%);
    color: #fff; font-size: 10px;
    display: flex; align-items: center; justify-content: center;
  }
  .contact-icon--phone { background: var(--icon-orange); }
  .contact-icon--email { background: var(--icon-green); }
</style>
</head>
<body>

<section class="card card--back">
  <div class="back-dots"><span></span><span></span></div>
  <div class="brand-name">KTV Holdings Ltd.</div>
</section>

<section class="card card--front">
  <div class="services">
    <div class="service-photos">
      <div class="service-photo service-photo--snow" role="img" aria-label="Photo of a red snowmobile"></div>
      <div class="service-photo service-photo--moto" role="img" aria-label="Photo of an orange sport motorcycle"></div>
    </div>
    <div class="service-types">SNOWMOBILE | MOTORCYCLE</div>
    <ul class="service-list">
      <li><svg width="22" height="18" viewBox="0 0 22 18"><rect x="1" y="4" width="13" height="13" fill="none" stroke="#b9c0c4" stroke-width="1.5"/><path d="M4 10l4 4 12-13" fill="none" stroke="#e6e6e6" stroke-width="2.5"/></svg>MAINTENANCE</li>
      <li><svg width="22" height="18" viewBox="0 0 22 18"><rect x="1" y="4" width="13" height="13" fill="none" stroke="#b9c0c4" stroke-width="1.5"/><path d="M4 10l4 4 12-13" fill="none" stroke="#e6e6e6" stroke-width="2.5"/></svg>SELLING</li>
      <li><svg width="22" height="18" viewBox="0 0 22 18"><rect x="1" y="4" width="13" height="13" fill="none" stroke="#b9c0c4" stroke-width="1.5"/><path d="M4 10l4 4 12-13" fill="none" stroke="#e6e6e6" stroke-width="2.5"/></svg>INSTALL PARTS<br>AND ACCESSORIES</li>
    </ul>
  </div>

  <div class="identity">
    <div class="brand-name">KTV Holdings Ltd.</div>
    <div class="person-name">MILO FENWICK</div>
    <p class="person-bio">I AM A JOURNEYMAN RED SEAL AUTOMOTIVE TECHNICIAN, JOURNEYMAN RED SEAL MOTORCYCLE TECHNICIAN AND JOURNEYMAN PARTS MAN.</p>
    <div class="contact-row"><span class="contact-icon contact-icon--phone">T</span>780-413-2769</div>
    <div class="contact-row contact-row--email"><span class="contact-icon contact-icon--email">E</span>KTVHOLD.77@TRAILMAIL.COM</div>
  </div>
</section>

</body>
</html>
```